Technical Communications firm needs an article turned into a white paper

We want to redesign a 3-part blog series into a white paper that we can print for a conference. I've consolidated the three posts into the attached Word document.

We are looking for a light, easy to read design. Good use of graphics to support the message. I've added the graphics we used in the original post.

You can view them at
http://www.quillmarrowgroup.com/blog/are-you-satisfied-with-your-dita-solution/

Target Market(s)

Product managers from High-tech, Finance, and Medical industries.

Industry/Entity Type

Information Technology

Colors

Designer to choose colors to be used in the design.

Requirements
Must have
• Must be modern, light, easy to read and slick design. Try to incorporate the graphics provided, but feel free to add more. Must retain the lists and tables.
• Must align with our website/brand.
• Must be easy to read. So not too busy.
• Please move all footnotes to endnotes. You'll need to rework the numbering.
Nice to have
• Awesome coverpage.
Should not have
• Hokey clipart. Not too heavy or hard to read.

```html
<!DOCTYPE html>
<html lang="en">
<head>
<meta charset="utf-8">
<title>White Paper – Are You Satisfied With Your DITA Solution?</title>
<link rel="stylesheet" href="https://fonts.googleapis.com/css2?family=Roboto:wght@300;400;500;700&display=swap">
<style>
:root{
  --bg:#ebebeb;
  --paper:#ffffff;
  --royal:#2b2bb0;
  --royal-deep:#1d1d8f;
  --cyan:#15a7dd;
  --pale:#cfe7f1;
  --lilac:#dcdcf3;
  --ink:#3a3a3a;
  --head:#2336a8;
}
*{margin:0;padding:0;box-sizing:border-box}
html,body{width:1200px;height:1200px;overflow:hidden;background:var(--bg);font-family:"Roboto",Arial,sans-serif;color:var(--ink)}
.stage{position:relative;width:1200px;height:1200px}
.page{position:absolute;width:307px;height:435px;background:var(--paper);overflow:hidden}
.hero{position:absolute;left:0;top:0;width:307px;height:122px}
.hero svg{position:absolute;left:0;top:0}
.hero-title{position:absolute;left:22px;color:#fff;font-weight:300;font-size:14px;line-height:16px;letter-spacing:.2px}
.hero-title b{font-weight:500}
.byline{position:absolute;left:20px;top:104px;color:#fff;font-size:4.6px;font-style:italic;line-height:5.6px}
.txt{position:absolute;font-size:4.6px;line-height:5.8px;color:var(--ink)}
.txt p{margin-bottom:4px;text-indent:8px}
.txt ul{margin:0 0 4px 8px}
.txt li{margin-bottom:2px}
.h{position:absolute;font-size:5.8px;font-weight:500;color:var(--head);padding-bottom:3px;border-bottom:1px solid #555}
.h::before{content:"";position:absolute;left:0;bottom:-1px;width:60%;height:2px;background:var(--cyan)}
.footer{position:absolute;left:0;bottom:0;width:307px;height:18px}
.footer span{position:absolute;right:40px;top:7px;font-size:4.2px;color:#fff}
.numbox{position:absolute;left:162px;width:132px;height:48px}
.numbox .n{position:absolute;left:4px;top:8px;font-size:26px;font-weight:300;color:var(--royal)}
.numbox .t{position:absolute;left:34px;top:5px;width:94px;font-size:4.3px;line-height:5.4px}
.numbox .t b{color:var(--royal);font-weight:500;display:block}
.grid{position:absolute;left:16px;top:16px;width:276px;border:1px solid #4a6bff}
.grid .row{display:flex;border-top:1px solid #4a6bff}
.grid .row:first-child{border-top:none}
.grid .cell{width:50%;padding:5px 8px;color:#fff;font-size:4.4px;line-height:5.4px;min-height:31px}
.grid .cell+.cell{border-left:1px solid #4a6bff}
.grid .th{font-size:6.8px;text-align:center;min-height:24px;padding-top:8px}
.step{position:absolute;top:276px;height:52px;width:60px;color:#fff;font-size:4.4px;line-height:5.4px;padding:4px 8px}
.step b{display:block;font-size:10px;font-weight:300;line-height:12px}
.step span{display:block;width:48px}
.conclusion{position:absolute;left:153px;top:246px;width:154px;height:166px;background:var(--royal-deep);color:#fff}
</style>
</head>
<body>
<div class="stage">

<!-- ===== PART 3 SPREAD ===== -->
<div class="page" style="left:534px;top:88px">
  <div class="hero">
    <svg width="307" height="122" viewBox="0 0 307 122">
      <defs><linearGradient id="sky3" x1="0" y1="0" x2="0" y2="1"><stop offset="0" stop-color="#9fb6cf"/><stop offset="1" stop-color="#e4e9ee"/></linearGradient></defs>
      <rect width="307" height="122" fill="url(#sky3)" role="img" aria-label="Photo of a tangle of yellow road signs against the sky"/>
      <rect x="168" y="12" width="120" height="92" fill="#e0b626" opacity=".55" role="img" aria-label="Cluster of direction signs"/>
      <polygon points="0,0 0,104 200,104" fill="var(--royal)" opacity=".95"/>
      <polygon points="0,104 206,104 196,122 0,122" fill="var(--royal-deep)"/>
      <rect x="196" y="118" width="111" height="2" fill="var(--cyan)"/>
    </svg>
    <div class="hero-title" style="top:56px"><b>PART 3:</b><br>MANAGEMENT</div>
    <div class="byline">By Dana Whitcombe – President of Quillmarrow Content<br>Authoring Group Inc.</div>
  </div>
  <div class="txt" style="left:30px;top:138px;width:115px"><p>This article is part of a series based on the results of a survey of more than 250 technical communication professionals conducted by The Copy Herder in 2017 entitled The DITA Satisfaction Survey[i]. In the survey, almost two-thirds of respondents voiced some concerns with their DITA deployment.</p><p>In my previous article in the series, I examined some of the principle issues related to technology.</p></div>
  <div class="txt" style="left:162px;top:124px;width:124px"><p>Organizations that see DITA as a magical fast-path to the bleeding edge of technology—or a panacea for multichannel publishing—are most likely to fail. Organizations that understand the importance of planning, experimentation and governance are more likely to experience success.</p></div>
  <div class="h" style="left:162px;top:168px;width:124px">Planning Strategies</div>
</div>

<div class="page" style="left:842px;top:88px">
  <div class="h" style="left:24px;top:45px;width:126px">Experimentation Strategies</div>
  <div class="txt" style="left:24px;top:64px;width:126px"><p>The importance of planned experimentation and how it plays into the growth of your structured authoring solution cannot be understated. Your experimentation begins with your first proof-of-concept (PoC) to demonstrate the advantages of structured authoring and validate your business case. Here it is important to keep your costs low and workplace disruption to a minimum. The success of your PoC should validate the costs for proceeding to the pilot.</p><p>Second phase of experimentation occurs with the design and execution of the pilot project. The pilot will rely on high-level use cases and target objectives determined during the PoC. This is still only an experimental stage. You may not want to be locked into any long-term commitments to one software vendor. Where possible, consider using subscription pricing and a hosted solution at least until the pilot has proven to be successful.</p><p>Once in production, consider conducting regular experiments on a staging server that remains isolated from your production systems.</p></div>
  <div class="txt" style="left:163px;top:30px;width:124px"><p>In 2015, Quillmarrow Content commissioned a study with InfoGuild entitled Innovating Content Creation and Reuse[v]. This study polled more than 300 organizations from around the world about their content creation practices and technology. When respondents were asked about content standards in place to manage content creation, 16% indicated there are strict standards in place, while 47% acknowledged there is something there, but not strictly followed. For 37% the indication was that there is little to no use of standards in any form.</p><p>Information Governance is the rocket fuel that empowers effective collaboration within and across teams and departments. Its purpose is to give everyone a voice in the future of the program and manage change across the enterprise. Good governance can be an important differentiator for your company.</p></div>
  <div class="h" style="left:163px;top:148px;width:124px;border:none">Quillmarrow Content® Information<br>Governance Workshop</div>
  <div class="txt" style="left:163px;top:168px;width:124px"><p>Let Quillmarrow Content help you build your governance strategy to engage both upper management and your team in a comprehensive, coordinated plan for moving forward with your structured authoring program. We'll help you to assess your maturity on the governance spectrum and lay out a path to a sustainable program. Working with our partners at InfoGuild, we will bring in industry-leading training and certification for your company to ensure success.</p></div>
  <svg style="position:absolute;left:153px;top:236px" width="154" height="12"><polygon points="0,12 154,0 154,12" fill="var(--cyan)"/></svg>
  <div class="conclusion">
    <div style="position:absolute;right:10px;top:6px;font-size:9px;font-weight:300">Conclusion</div>
    <div style="position:absolute;left:0;top:18px;width:154px;height:1px;background:#6f8cff"></div>
    <div class="txt" style="left:10px;top:24px;width:136px;color:#fff"><p>Don't let dissatisfaction derail your DITA project. Your greatest advancements in information management still to be achieved may not lie in the technology you use to manage content but in the content itself. Hundreds of companies have been working with structured authoring practices for producing intelligent content for more than a decade and found ways to reduce many of barriers to adoption including cost and complexity. You need not look too far to find practical advice and leverage lessons learned to bring their success into your organization. While this journey may seem daunting, it is one that should be taken seriously with a focus to begin with one element, and grow it out from there. The experts at Quillmarrow Authoring Group are pleased to support your journey and to share their knowledge.</p></div>
    <div style="position:absolute;left:10px;top:140px;font-size:5px;color:#9fd4ff">Call us today to help</div>
    <div style="position:absolute;left:10px;top:148px;font-size:6px;font-weight:700;font-style:italic">Put Your Content to Work.</div>
  </div>
  <div class="footer"><svg width="307" height="18"><polygon points="145,0 307,0 307,18 132,18" fill="var(--cyan)"/></svg><span>Quillmarrow Content 2017 | PAGE 7</span></div>
</div>

<!-- ===== PART 2 SPREAD ===== -->
<div class="page" style="left:370px;top:278px">
  <div class="hero">
    <svg width="307" height="122" viewBox="0 0 307 122">
      <defs><linearGradient id="sky2" x1="0" y1="0" x2="0" y2="1"><stop offset="0" stop-color="#8a8f96"/><stop offset="1" stop-color="#dfe1e3"/></linearGradient></defs>
      <rect width="307" height="122" fill="url(#sky2)" role="img" aria-label="Photo of an anchor lifted by a red balloon over a grey sea"/>
      <polygon points="0,0 0,104 200,104" fill="var(--royal)" opacity=".95"/>
      <polygon points="0,104 206,104 196,122 0,122" fill="var(--royal-deep)"/>
      <rect x="196" y="118" width="111" height="2" fill="var(--cyan)"/>
    </svg>
    <div class="hero-title" style="top:56px"><b>PART 2:</b><br>TECHNOLOGY</div>
    <div class="byline">By Dana Whitcombe – President of Quillmarrow Content<br>Authoring Group Inc.</div>
  </div>
  <div class="txt" style="left:22px;top:138px;width:120px"><p>This article is part of a series based on the results of a survey of more than 250 technical communication professionals conducted by The Copy Herder in 2017 entitled The DITA Satisfaction Survey[i]. In the survey, almost two-thirds of respondents voiced some concerns with their DITA deployment.</p><p>In my previous article, I examined some of the principal issues related to skills development. This article looks at how technology affects DITA satisfaction.</p></div>
  <div class="txt" style="left:162px;top:130px;width:124px"><p>Before we look at changing your technology, we should examine some of these problems to see if we can identify a more appropriate root cause.</p></div>
  <div style="position:absolute;left:158px;top:150px;width:134px;height:80px;background:#f1f2f6"></div>
  <div class="h" style="left:164px;top:154px;width:122px">Performance Problems</div>
  <div class="txt" style="left:164px;top:174px;width:122px"><p>Common complaints regarding performance include observations that processes take longer or systems are slower to respond than they were before the move to DITA. Part of this observation may be related to adjusting to different expectations.</p></div>
  <div class="footer"><svg width="307" height="18"><polygon points="145,0 307,0 307,18 132,18" fill="var(--cyan)"/></svg><span>Quillmarrow Content 2017 | PAGE 2</span></div>
</div>

<div class="page" style="left:677px;top:278px">
  <div class="h" style="left:24px;top:28px;width:126px">Complexity Problems</div>
  <div class="txt" style="left:24px;top:46px;width:126px"><p>Finding the correct balance of complexity versus utility is one of the biggest challenges we face in DITA deployments. The problem may not be that your tools are too complex, rather that too much complexity is exposed to the wrong group of users. The best-architected systems attempt to push the most complexity onto the shoulders of the fewest number of people. As much as possible, let the software handle most of the heavy lifting.</p><p>It's important to note that collaborative, structured authoring is always going to be more complex than traditional desktop publishing. Despite attempts to simplify the technology around content authoring, content itself is not getting any simpler. Ellis Marrow of Veridane Research believes that content development practices and technology are following trends we see in other related industries. His predictions are that content development will continue to become much more[ii]</p></div>
  <div class="txt" style="left:162px;top:48px;width:124px"><ul><li>precise</li><li>complex</li><li>collaborative, and</li><li>integrated into larger enterprise systems.</li></ul><p>To strike the proper balance between complexity and utility you need to consider how the technology decisions you make now impact the viability of your content in the future. Will simpler structures, semantics, and metadata cause significant rework in the future to attain your goals? Or, will postponing certain complexities increase the likelihood for adoption and pave the way for early wins? The only way to answer these questions is to map out your long-term goals and assess the steps you will take to get there.</p></div>
  <div class="h" style="left:24px;top:183px;width:262px">Steps to address complexity</div>
  <div class="txt" style="left:162px;top:208px;width:124px"><p>ties you need to achieve over the next two years. Your strategy should align with your business goals and direction. Plan for a minor review every 6 months and a major review each year to determine your funding requirements to stay the course with your roadmap.</p><p>By understanding your plan and getting sign-off from stakeholders, you will be able to determine whether you should:</p></div>
  <div class="step" style="left:80px;width:58px;background:var(--cyan);clip-path:polygon(10% 0,100% 0,90% 100%,0 100%)"><b>3</b><span>invest more time and money in training to compensate for complexity</span></div>
  <div class="step" style="left:134px;width:60px;background:var(--lilac);color:#444;clip-path:polygon(10% 0,100% 0,90% 100%,0 100%)"><b style="color:var(--royal)">4</b><span>invest more money in tools that better mask the complexity, or</span></div>
  <div class="step" style="left:190px;width:117px;background:var(--cyan);clip-path:polygon(5% 0,100% 0,100% 100%,0 100%)"><b>5</b><span>re-engineer certain aspects of your processes.</span></div>
  <div class="txt" style="left:162px;top:340px;width:124px"><p>that as well. Sometimes we all just need to stop throwing more technology at our content problems. Learn more about our workshops.</p></div>
  <div class="footer"><svg width="307" height="18"><polygon points="145,0 307,0 307,18 132,18" fill="var(--cyan)"/></svg><span>Quillmarrow Content 2017 | PAGE 5</span></div>
</div>

<!-- ===== PART 1 SPREAD ===== -->
<div class="page" style="left:190px;top:481px">
  <div class="hero">
    <svg width="307" height="122" viewBox="0 0 307 122">
      <defs><linearGradient id="board1" x1="0" y1="0" x2="1" y2="1"><stop offset="0" stop-color="#2f7a55"/><stop offset="1" stop-color="#5aa07a"/></linearGradient></defs>
      <rect width="307" height="122" fill="url(#board1)" role="img" aria-label="Photo of a puzzled man in front of a chalkboard asking what he is supposed to do"/>
      <polygon points="0,0 0,104 200,104" fill="var(--royal)" opacity=".95"/>
      <polygon points="0,104 206,104 196,122 0,122" fill="var(--royal-deep)"/>
      <rect x="196" y="118" width="111" height="2" fill="var(--cyan)"/>
    </svg>
    <div class="hero-title" style="top:34px"><b>PART 1:</b><br>SKILLS<br>DEVELOPMENT</div>
    <div class="byline">By Dana Whitcombe – President of Quillmarrow Content<br>Authoring Group Inc.</div>
  </div>
  <div class="txt" style="left:22px;top:134px;width:120px"><p>This article is part of a series based on the results of a survey of more than 250 technical communication professionals conducted by The Copy Herder in 2017 entitled The DITA Satisfaction Survey[i]. In the survey, almost two-thirds of respondents voiced some concerns with their DITA deployment.</p></div>
  <div class="txt" style="left:162px;top:134px;width:124px"><p>In our previous article, we introduced the overall results from the survey that pertain to users' dissatisfaction with their DITA solution. In this article, we examine the top rated issues pertaining to skills development.</p></div>
  <div class="txt" style="left:162px;top:203px;width:124px"><p>Many teams invest in tools training—and may even opt for a basic authoring course to learn about DITA—but they rarely take the effort to train writers how to author modular, structured topics of content designed for reuse.</p><p>It is easy to overlook this training aspect and assume that writers will naturally adapt to this new way of writing. But, those assumptions can lead to big problems.</p><p>A poll conducted in a recent webinar[ii] where half of the participants indicated they were already using DITA, a full 70% indicated that they had no formal DITA training. Of those participants, nearly 60% were struggling while the others had no training at all. It's no wonder that dissatisfaction is the norm.</p></div>
  <div class="txt" style="left:162px;top:328px;width:124px"><p>These resources demonstrate how to markup content, but they often not teach you how to rethink and restructure your content to take advantage of DITA's capabilities. Consider the differences between structured writing and structured markup.</p></div>
  <div class="footer"><svg width="307" height="18"><polygon points="145,0 307,0 307,18 132,18" fill="var(--cyan)"/></svg><span>Quillmarrow Content 2017 | PAGE 2</span></div>
</div>

<div class="page" style="left:496px;top:481px">
  <div style="position:absolute;left:0;top:0;width:307px;height:199px;background:var(--royal-deep)"></div>
  <div class="grid">
    <div class="row"><div class="cell th">Structured Writing</div><div class="cell th">Structured Markup</div></div>
    <div class="row"><div class="cell">• Coined by Martin Crale in the 1960's as a means of analyzing, organizing, and presenting information for optimal human consumption</div><div class="cell">• Allows authors to markup words, phrases, and sections of content for presentation and for meaning for consumption by machines</div></div>
    <div class="row"><div class="cell">• Promotes patterns for format and syntax that become easily recognizable and predictable</div><div class="cell">• Is validated using standard sets of rules that specify consistent and predictable patterns</div></div>
    <div class="row"><div class="cell">• Relies on consistently labelling and chunking information into easily scannable text</div><div class="cell">• Specifies what content goes where but does not limit or restrict how the content is written</div></div>
    <div class="row"><div class="cell">• Introduces universal information typing based on intended reader response</div><div class="cell">• Provides a rich underlying metadata layer for capturing properties related to the content</div></div>
  </div>
  <div style="position:absolute;left:22px;top:187px;font-size:4.2px;font-style:italic;color:#fff">Table reproduced from "Driving Enterprise Productivity from the Front of the DITA XML Train[iii]"</div>
  <div class="h" style="left:22px;top:216px;width:124px">Continuous Collaborative Learning</div>
  <div class="txt" style="left:22px;top:236px;width:120px"><p>Organizations that wisely invest in comprehensive training for their writing teams also recognize the importance of continuous learning and recurring training. To stay on top of knowledge sharing in your team, consider the following collaboration activities:</p><ul><li>Schedule regular checkpoints where your team discusses what they've learned with other members of the team.</li><li>Assign different members of your team to research and present best practices at regularly scheduled lunch-and-learn sessions.</li></ul></div>
  <div class="txt" style="left:162px;top:236px;width:124px"><ul><li>Attend webinars and seminars on best practices as a group and then debrief together to discuss aspects that should be incorporated into your day-to-day work.</li><li>Review and update your content standards regularly as a team to keep your procedures and guidelines current and relevant.</li><li>Pair up senior members of your team with new or junior members for regular mentoring and coaching.</li></ul></div>
  <div class="h" style="left:22px;top:324px;width:264px">Quillmarrow Content® Structured Author Training</div>
  <div class="txt" style="left:22px;top:344px;width:120px"><p>Quillmarrow Content has many years of experience teaching organizations how to write better structured content. Our inhouse, instructor-led training courses run from 1 to 5 days depending on your needs and cover the gamut of tools and techniques</p></div>
  <div class="txt" style="left:162px;top:344px;width:124px"><p>needed for successful structured authoring. Learn more about our DITA training. Or contact Quillmarrow Content to find out more about how we can address your specific training needs.</p></div>
  <div class="footer"><svg width="307" height="18"><polygon points="145,0 307,0 307,18 132,18" fill="var(--cyan)"/></svg><span>Quillmarrow Content 2017 | PAGE 3</span></div>
</div>

<!-- ===== COVER ===== -->
<div class="page" style="left:62px;top:664px;width:308px;height:434px">
  <div class="hero" style="width:308px;height:120px">
    <svg width="308" height="122" viewBox="0 0 308 122">
      <defs><linearGradient id="board0" x1="0" y1="0" x2="1" y2="0"><stop offset="0" stop-color="#4b5559"/><stop offset="1" stop-color="#6d7679"/></linearGradient></defs>
      <rect width="308" height="120" fill="url(#board0)" role="img" aria-label="Photo of a thoughtful man beside a chalkboard checklist rated with stars"/>
      <polygon points="0,0 0,102 198,102" fill="var(--royal)" opacity=".9"/>
      <polygon points="0,102 204,102 194,120 0,120" fill="var(--royal-deep)"/>
      <rect x="194" y="116" width="114" height="2" fill="var(--cyan)"/>
      <g fill="none" stroke="#fff" stroke-width=".8">
        <rect x="166" y="22" width="6" height="6"/><rect x="166" y="42" width="6" height="6"/><rect x="166" y="62" width="6" height="6"/><rect x="166" y="82" width="6" height="6"/>
        <path d="M166 82 L172 88 M172 82 L166 88"/>
      </g>
    </svg>
    <div class="hero-title" style="top:28px;font-size:14.5px;line-height:17px">ARE YOU<br>SATISFIED<br>WITH YOUR<br>DITA SOLUTION?</div>
    <div class="byline" style="top:102px">By Dana Whitcombe – President of Quillmarrow Content<br>Authoring Group Inc.</div>
  </div>
  <div class="txt" style="left:22px;top:138px;width:118px"><p>If your answer is "No" then you are not alone according to a 2017 survey of more than 250 technical communication professionals conducted by The Copy Herder. The DITA Satisfaction Survey[i] indicates that 62% of respondents using DITA are—to varying degrees—dissatisfied. As many as 10% of that group were very dissatisfied reporting that their DITA implementation is experiencing 'big' challenges. It's not surprising that there's significant dissatisfaction amongst those who have adopted DITA. After all, moving to DITA is a seismic shift in technical writing; a big change with many opportunities for things to go wrong.</p><p>The good news is that most DITA users don't see their problems as insurmountable. Many just need a little help getting to where they'd like to be.</p></div>
  <div class="h" style="left:22px;top:264px;width:116px">Breakdown of the issues</div>
  <div class="txt" style="left:22px;top:284px;width:118px"><p>The Copy Herder DITA Satisfaction Survey asked respondents to rank the top 10 issues facing DITA users. These issues fit into three major categories including</p><ul><li>skills development</li><li>technology, and</li><li>management.</li></ul><p>The DITA Satisfaction Survey Aggregate Results revealed little spread between the ranking of the issues indicating that respondents likely faced more than one issue of concern.</p></div>
  <div class="h" style="left:162px;top:140px;width:132px">In this article</div>
  <div class="txt" style="left:162px;top:158px;width:132px"><p>In this article, we examine three issues impacting DITA satisfaction to help you find the best place to start making improvements.</p></div>
  <div class="numbox" style="top:192px"><svg width="132" height="48"><polygon points="0,0 132,0 132,48 0,48 18,24" fill="var(--pale)"/></svg><div class="n">1</div><div class="t"><b>Part 1: Skills Development –</b>This problem area is far and away the most pressing obstacle for a successful DITA deployment. Too often authors are left to figure out how to adapt to writing for DITA on their own.</div></div>
  <div class="numbox" style="top:252px;"><svg width="132" height="48"><polygon points="0,0 132,0 132,48 0,48 18,24" fill="#fff"/></svg><div class="n">2</div><div class="t"><b>Part 2: Technology –</b>We often hear about the failure of the technology as it relates to performance or complexity. While technology may seem the most likely culprit, it is often not the root cause of the problem.</div></div>
  <div class="numbox" style="top:314px;height:62px"><svg width="132" height="62"><polygon points="0,0 132,0 132,62 0,62 18,31" fill="var(--pale)"/></svg><div class="n" style="top:14px">3</div><div class="t"><b>Part 3: Management –</b>While these issues appear to be of least concern to many survey respondents, they are most likely to form the root cause of all other issues identified in the survey. This points to a general lack of awareness as to the role management should be playing in collaborative, structured authoring solutions.</div></div>
  <div class="footer" style="width:308px"><svg width="308" height="18"><polygon points="150,0 308,0 308,18 136,18" fill="var(--cyan)"/></svg><span>Quillmarrow Content 2017 | PAGE 1</span></div>
</div>

</div>
</body>
</html>
```